Book Cover for Collection of Dark Short Stories

I need a cover design for my book "Amber Hollows." It will be a 5 x 8 paperback roughly 200 pages long. There will be 11 short stories in it of a darker nature. The book is a mixture of science fiction, historical fiction, and just interesting to read stories. The stories focus on individuals or people facing difficult situations such as terrifying end of the world scenarios, mortal danger in wars, as well as crushing debt and a job layoff.
I envision the cover with dark colors (blue/black). One suggestion is to have the silhouette of a man outside sitting on a log or hill with him looking slightly down in contemplation. There are dark clouds covering most of the sky, but the stars and/or moon are trying to shine through in one small area. There's a small amount of hope in the gloom.
I see the mood of the cover as darkly reflective.

I will be happy to look at other suggestions, too.

I will also have some text on the back with a small author photo in the middle. I see the back cover as a continuation of the front cover with dark clouds and again the small amount of light from the moon and stars.
I don't want any violence or death in the cover.
I'll be happy to look at suggestions for the back cover area from the designers.

The title of the book is: AMBER HOLLOWS a subtitle in a smaller font somewhere below should read: A Collection of Short Stories My name should be at the bottom of the cover: Dana Whitcombe

Hey designers, Please find the text for the back cover here: This fascinating collection of short stories is a unique blend of science fiction, action, and historical fiction that will entertain and challenge you. In Amber Hollows’ 11 intriguing stories, we experience one isolated man’s survival as he holds out and awaits the terrifying arrival of otherworldly visitors; firsthand battlefield accounts with some strange occurrences in both WW II and the Revolutionary War; and a tiger hunt in India that goes very wrong. We also see tales of modern woe revolving around some of life’s common miseries, accompanied by brave and unexpected measures to fight against them. In addition, we witness an awkward and dangerous stay in an underground bunker with an unstable host; two astronauts stranded on a lifeless asteroid who only have one old-fashioned form of entertainment; an eerie post-plague world dominated by an unlikely species; and an eccentric astronaut orbiting the Earth who is happiest on his own, except for one furry exception. Dana Whitcombe’s interesting stories travel in different directions, but spring from one deep source: the darker side of the imagination. I also have an author photo that I would like either below the text or in between, whichever looks better. Feel free to crop it without my hands or whatever looks best.

Target Market(s)

Men 18-65, but crossover appeal to women is fine, too.

Font styles to use
Serif

Colors
0255a3
000000
1b1b1b
dcdcdc
fbf289

Requirements
Must have
• AMBER HOLLOWS in some form.
Nice to have
• Some interesting takes on AMBER HOLLOWS and the silhouette of a man sitting and contemplating deep things (like the end of the world).
Should not have
• No violence, sex, death, or anything provocative in the cover. I want to convey a serious, dark contemplative mood with a slight amount of hope.

```html
<!DOCTYPE html>
<html lang="en">
<head>
<meta charset="utf-8">
<title>Amber Hollows — Cover Wrap</title>
<link rel="stylesheet" href="https://fonts.googleapis.com/css2?family=Oswald:wght@600;700&family=Cinzel:wght@400&family=Tinos&display=swap">
<style>
  :root {
    --page-bg: #dcdcdc;
    --sky-deep: #0b1526;
    --sky-mid: #2c4a7e;
    --sky-light: #6f8dc0;
    --sky-teal: #3c5a5a;
    --ground: #050505;
    --glow: #fbf289;
    --blurb-panel: #4f6c9f;
    --blurb-band: #2d4248;
    --ink-light: #ffffff;
    --ink-soft: #f1f3f8;
  }
  * { margin: 0; padding: 0; box-sizing: border-box; }
  html, body { width: 1200px; height: 1200px; overflow: hidden; background: var(--page-bg); }

  .cover-wrap {
    position: absolute;
    left: 40px; top: 171px;
    width: 1120px; height: 857px;
    overflow: hidden;
  }

  .cover-art {
    position: absolute; inset: 0;
    background:
      radial-gradient(ellipse 90px 70px at 100px 715px, rgba(251,242,137,.75), rgba(251,242,137,0) 100%),
      radial-gradient(ellipse 520px 160px at 260px 740px, rgba(150,110,50,.55), rgba(0,0,0,0) 100%),
      radial-gradient(ellipse 380px 300px at 830px 430px, rgba(140,170,220,.55), rgba(0,0,0,0) 100%),
      radial-gradient(ellipse 300px 240px at 980px 120px, rgba(70,110,110,.55), rgba(0,0,0,0) 100%),
      linear-gradient(180deg, var(--sky-deep) 0%, var(--sky-mid) 35%, var(--sky-light) 55%, var(--sky-mid) 75%, var(--ground) 100%);
  }
  .cover-art::after {
    content: ""; position: absolute; left: 0; right: 0; bottom: 0; height: 60px;
    background: linear-gradient(180deg, rgba(5,5,5,0), var(--ground));
  }

  .back-blurb {
    position: absolute;
    left: 30px; top: 51px;
    width: 476px; height: 630px;
    background: var(--blurb-panel);
  }
  .back-blurb__title {
    font-family: "Oswald", sans-serif;
    font-weight: 700;
    font-size: 29px;
    letter-spacing: .3px;
    color: var(--ink-light);
    text-align: center;
    padding-top: 16px;
    line-height: 1.2;
  }
  .back-blurb__text {
    font-family: "Tinos", serif;
    font-size: 16.4px;
    line-height: 21.4px;
    color: var(--ink-soft);
    padding: 6px 26px 0 28px;
  }
  .wrap-spacer { float: right; width: 0; height: 352px; }
  .wrap-portrait { float: right; clear: right; width: 188px; height: 220px; }
  .back-blurb__band {
    position: absolute; left: 0; bottom: 0;
    width: 300px; height: 31px;
    background: var(--blurb-band);
  }
  .author-portrait {
    position: absolute; right: 0; bottom: 0;
    width: 176px; height: 195px;
    background: linear-gradient(160deg, #5b6f86 0%, #2b3444 60%, #1b1b1b 100%);
  }

  .spine {
    position: absolute;
    left: 482px; top: 0;
    width: 70px; height: 857px;
  }
  .spine__title, .spine__author {
    position: absolute; left: 50%;
    writing-mode: vertical-rl;
    transform: translateX(-50%);
    color: var(--ink-light);
    white-space: nowrap;
  }
  .spine__title {
    top: 54px;
    font-family: "Oswald", sans-serif;
    font-weight: 700;
    font-size: 30px;
  }
  .spine__author {
    top: 535px;
    font-family: "Cinzel", serif;
    font-size: 30px;
    letter-spacing: 1px;
  }

  .front {
    position: absolute;
    left: 552px; top: 0;
    width: 568px; height: 857px;
    text-align: center;
    color: var(--ink-light);
  }
  .front__title {
    position: absolute; left: 0; right: 0; top: 40px;
    font-family: "Oswald", sans-serif;
    font-weight: 700;
    font-size: 138px;
    line-height: 128px;
    letter-spacing: -2px;
    text-shadow: 0 4px 10px rgba(0,0,0,.55);
  }
  .front__subtitle {
    position: absolute; left: 0; right: 0; top: 312px;
    font-family: "Cinzel", serif;
    font-size: 24px;
    letter-spacing: .8px;
  }
  .front__author {
    position: absolute; left: 0; right: 0; top: 778px;
    font-family: "Cinzel", serif;
    font-size: 38px;
    letter-spacing: 1.5px;
  }
</style>
</head>
<body>
  <main class="cover-wrap">
    <div class="cover-art" role="img" aria-label="Dark stormy night sky of blue clouds with a faint glowing moon and stars near the horizon, and the silhouette of a man sitting on a grassy hill looking down in contemplation"></div>

    <section class="back-blurb">
      <h2 class="back-blurb__title">AMBER HOLLOWS</h2>
      <p class="back-blurb__text"><span class="wrap-spacer"></span><span class="wrap-portrait"></span>This fascinating collection of short stories is a unique blend of science fiction, action, and historical fiction that will entertain and challenge you. In Amber Hollows’ 11 intriguing stories, we experience one isolated man’s survival as he holds out and awaits the terrifying arrival of otherworldly visitors; firsthand battlefield accounts with some strange occurrences in both WW II and the Revolutionary War; and a tiger hunt in India that goes very wrong. We also see tales of modern woe revolving around some of life’s common miseries, accompanied by brave and unexpected measures to fight against them. In addition, we witness an awkward and dangerous stay in an underground bunker with an unstable host; two astronauts stranded on a lifeless asteroid who only have one old-fashioned form of entertainment; an eerie post-plague world dominated by an unlikely species; and an eccentric astronaut orbiting the Earth who is happiest on his own, except for one furry exception. Dana Whitcombe’s interesting stories travel in different directions, but spring from one deep source: the darker side of the imagination.</p>
      <div class="back-blurb__band"></div>
      <div class="author-portrait" role="img" aria-label="Author portrait photo, head and shoulders in a dark suit and tie"></div>
    </section>

    <aside class="spine">
      <span class="spine__title">AMBER HOLLOWS</span>
      <span class="spine__author">DANA WHITCOMBE</span>
    </aside>

    <section class="front">
      <h1 class="front__title">AMBER<br>HOLLOWS</h1>
      <p class="front__subtitle">A COLLECTION OF SHORT STORIES</p>
      <p class="front__author">DANA WHITCOMBE</p>
    </section>
  </main>
</body>
</html>
```